Mobile Game identical to "Letter Orbit"

We need a design for mobile game identical to "Letter Orbit" you can get from app store using this link https://quickstorelink.example/us/tzvnR.k
playstore link: https://apps.samplemarket.example/store/apps/details?id=se.fenwoodgames.letterorbit&hl=en

- App name will be : Tangle
- For iOS and Android
- Same Letter Orbit features exactly but in different design.
- Ads banner will be overall app screens
- Some kind of animation is needed in the game , designer has to provide.

Requirements
Must have
• - Same Letter Orbit Features and steps
• - Some Animation
• - Game will be in arabic i will help to provide needed text

```html
<!DOCTYPE html>
<html lang="en">
<head>
<meta charset="utf-8">
<title>Tangle – Game Screen</title>
<link rel="stylesheet" href="https://fonts.googleapis.com/css2?family=Montserrat:wght@500;600;700&display=swap">
<style>
  :root {
    --bg-top: #3d4190;
    --bg-bottom: #2c2d6b;
    --tile: #4b509e;
    --tile-solved: #6cbc4b;
    --letter: #ffffff;
    --letter-solved: #f2f5d9;
    --slot-line: #6b6fb8;
    --accent: #e9dc6f;
    --text: #ffffff;
  }
  * { box-sizing: border-box; margin: 0; padding: 0; }
  html, body { width: 720px; height: 1200px; overflow: hidden; }
  body {
    font-family: "Montserrat", Arial, sans-serif;
    color: var(--text);
    background: linear-gradient(180deg, var(--bg-top) 0%, var(--bg-bottom) 100%);
    position: relative;
  }
  .status-bar {
    position: absolute; top: 0; left: 0; right: 0; height: 50px;
    display: flex; align-items: center; justify-content: space-between;
    padding: 0 26px; font-size: 20px; font-weight: 600;
  }
  .status-left, .status-right { display: flex; align-items: center; gap: 10px; width: 220px; white-space: nowrap; }
  .status-right { justify-content: flex-end; }
  .status-time { font-weight: 700; }
  .app-header {
    position: absolute; top: 70px; left: 0; right: 0; height: 60px;
    display: flex; align-items: center; justify-content: space-between; padding: 0 34px;
  }
  .screen-title { font-size: 22px; font-weight: 700; letter-spacing: 1.5px; }
  .letter-grid {
    position: absolute; top: 230px; left: 95px;
    display: grid; grid-template-columns: repeat(3, 158px); gap: 28px;
  }
  .tile {
    width: 158px; height: 158px; border-radius: 8px;
    background: var(--tile);
    display: flex; align-items: center; justify-content: center;
    font-size: 74px; font-weight: 600; color: var(--letter);
  }
  .tile--solved { background: var(--tile-solved); color: var(--letter-solved); }
  .answer-slots {
    position: absolute; top: 850px; left: 0; right: 0;
    display: flex; justify-content: center; gap: 40px;
  }
  .word-slots { display: flex; gap: 8px; }
  .slot { width: 48px; height: 52px; border: 3px solid var(--slot-line); border-radius: 6px; }
  .controls {
    position: absolute; top: 1000px; left: 0; right: 0;
    display: flex; justify-content: center; gap: 36px;
  }
  .control {
    height: 96px; border: 4px solid var(--accent); border-radius: 22px;
    display: flex; align-items: center; justify-content: center;
    color: var(--accent); font-weight: 700;
  }
  .control--help { width: 132px; font-size: 54px; }
  .control--reset { width: 104px; }
  .control--hint { width: 210px; font-size: 34px; letter-spacing: 1px; }
</style>
</head>
<body>
  <div class="status-bar">
    <div class="status-left">
      <svg width="52" height="12" viewBox="0 0 52 12"><g fill="#fff"><circle cx="6" cy="6" r="5"/><circle cx="16" cy="6" r="5"/><circle cx="26" cy="6" r="5"/><circle cx="36" cy="6" r="4.5" fill="none" stroke="#fff" stroke-width="1.2"/><circle cx="46" cy="6" r="4.5" fill="none" stroke="#fff" stroke-width="1.2"/></g></svg>
      <span>CARRIER</span>
      <svg width="20" height="16" viewBox="0 0 20 16"><path d="M10 15 L2 6 A12 12 0 0 1 18 6 Z" fill="#fff"/></svg>
    </div>
    <span class="status-time">4:21 PM</span>
    <div class="status-right">
      <svg width="12" height="20" viewBox="0 0 12 20"><path d="M1 5 L11 15 L6 19 V1 L11 5 L1 15" fill="none" stroke="#fff" stroke-width="1.8"/></svg>
      <span>100%</span>
      <svg width="44" height="20" viewBox="0 0 44 20"><rect x="1" y="1" width="38" height="18" rx="4" fill="none" stroke="#fff" stroke-width="2"/><rect x="4" y="4" width="32" height="12" rx="2" fill="#fff"/><rect x="40" y="7" width="3" height="6" rx="1" fill="#fff"/></svg>
    </div>
  </div>

  <header class="app-header">
    <svg class="icon-back" width="36" height="36" viewBox="0 0 36 36"><circle cx="18" cy="18" r="15" fill="none" stroke="#fff" stroke-width="3"/><path d="M21 11 L14 18 L21 25" fill="none" stroke="#fff" stroke-width="3" stroke-linecap="round" stroke-linejoin="round"/></svg>
    <h1 class="screen-title">TANGLE</h1>
    <svg class="icon-profile" width="36" height="36" viewBox="0 0 36 36"><circle cx="18" cy="18" r="15" fill="none" stroke="#fff" stroke-width="3"/><circle cx="18" cy="14" r="5" fill="none" stroke="#fff" stroke-width="2.6"/><path d="M9 28 C11 21 25 21 27 28" fill="none" stroke="#fff" stroke-width="2.6"/></svg>
  </header>

  <main class="letter-grid">
    <div class="tile tile--solved">F</div>
    <div class="tile">L</div>
    <div class="tile">O</div>
    <div class="tile tile--solved">P</div>
    <div class="tile tile--solved">O</div>
    <div class="tile">S</div>
    <div class="tile tile--solved">Y</div>
    <div class="tile">C</div>
    <div class="tile">J</div>
  </main>

  <div class="answer-slots">
    <div class="word-slots"><span class="slot"></span><span class="slot"></span><span class="slot"></span><span class="slot"></span></div>
    <div class="word-slots"><span class="slot"></span><span class="slot"></span><span class="slot"></span></div>
  </div>

  <nav class="controls">
    <div class="control control--help">?</div>
    <div class="control control--reset">
      <svg width="50" height="50" viewBox="0 0 50 50"><path d="M38 18 A15 15 0 1 0 40 28" fill="none" stroke="#e9dc6f" stroke-width="5" stroke-linecap="round"/><path d="M30 17 L40 18 L40 8" fill="none" stroke="#e9dc6f" stroke-width="5" stroke-linecap="round" stroke-linejoin="round"/></svg>
    </div>
    <div class="control control--hint">HINT</div>
  </nav>
</body>
</html>
```